Harrowgate Supply Group Business Card Design

The Business Card will be one side only with Harrowgate Supplies Group Logo
Card should have:
Name
Title
Office phone Number
Cell Number
email address
Website
Street Address
Our Slogan is Heavy Duty, Every Day
Looking for something that stands out from other business cards

Target Market(s)

Heavy equipment Lease Company

```html
<!DOCTYPE html>
<html lang="en">
<head>
<meta charset="utf-8">
<title>Harrowgate Supplies Group Business Card</title>
<link rel="stylesheet" href="https://fonts.googleapis.com/css2?family=Montserrat:wght@700&family=Open+Sans:wght@400;600&display=swap">
<style>
  :root {
    --page-bg: #2b3036;
    --card-bg: #231f20;
    --brand-red: #d11a2a;
    --brand-blue: #28278a;
    --text-white: #ffffff;
    --text-grey: #c9c9c9;
    --text-muted: #9a9a9a;
  }
  * { margin: 0; padding: 0; box-sizing: border-box; }
  html, body {
    width: 1200px;
    height: 900px;
    overflow: hidden;
    background: var(--page-bg);
  }
  .stage {
    width: 1200px;
    height: 900px;
    display: flex;
    align-items: center;
    justify-content: center;
  }
  .business-card {
    position: relative;
    width: 1050px;
    height: 600px;
    background: var(--card-bg);
    overflow: hidden;
    box-shadow: 0 20px 50px rgba(0,0,0,0.45);
  }
  .card-art {
    position: absolute;
    inset: 0;
  }
  .brand {
    position: absolute;
    left: 56px;
    top: 44px;
    display: flex;
    align-items: center;
    gap: 12px;
  }
  .brand-dot {
    width: 30px;
    height: 30px;
    border-radius: 50%;
    background: var(--brand-blue);
  }
  .brand-name {
    font-family: "Montserrat", sans-serif;
    font-weight: 700;
    font-size: 22px;
    letter-spacing: 0.5px;
    color: var(--brand-red);
  }
  .contact {
    position: absolute;
    left: 56px;
    top: 110px;
    font-family: "Open Sans", sans-serif;
  }
  .person-name {
    font-family: "Montserrat", sans-serif;
    font-weight: 700;
    font-size: 30px;
    color: var(--text-white);
  }
  .person-title {
    font-size: 18px;
    color: var(--text-muted);
    margin-top: 2px;
  }
  .contact-list {
    list-style: none;
    margin-top: 26px;
  }
  .contact-list li {
    font-size: 19px;
    line-height: 31px;
    color: var(--text-grey);
    letter-spacing: 0.4px;
  }
  .slogan {
    position: absolute;
    left: 600px;
    top: 210px;
    font-family: "Montserrat", sans-serif;
    font-weight: 700;
    font-size: 34px;
    color: var(--text-white);
  }
</style>
</head>
<body>
<main class="stage">
  <article class="business-card">
    <svg class="card-art" width="1050" height="600" viewBox="0 0 1050 600" aria-hidden="true">
      <polygon class="blue-field" points="600,600 1050,360 1050,600" fill="#28278a"/>
      <rect class="red-band" x="0" y="556" width="560" height="14" fill="#d11a2a"/>
    </svg>

    <div class="brand">
      <span class="brand-dot"></span>
      <span class="brand-name">HARROWGATE SUPPLIES GROUP</span>
    </div>

    <section class="contact">
      <h1 class="person-name">Your Name</h1>
      <p class="person-title">Title</p>
      <ul class="contact-list">
        <li>999 999 9999</li>
        <li>999 999 9999</li>
        <li>email@website.com</li>
        <li>www.website.com</li>
        <li>Street Address</li>
      </ul>
    </section>

    <p class="slogan">Heavy Duty, Every Day</p>
  </article>
</main>
</body>
</html>
```